Web Design

We need a new website for our company. We perform several functions:

1 - IT and Network Support
2 - Computer Consultancy
3 - Cloud Services
4 - Hosted Mailvane & Online Backup
5 - Internet Connections & VOIP

Examples of some of the designs we like can be seen on:
• www.brelvox.com
• www.quintaro.com

I urgently need a new website to be designed to enable me to look more professional. My competitors website is www.tdmq.co.uk

I also want to be able to look much more professional, like www.brelvox.com www.quintaro.com

I have attached how I would like the website to look

Task outline
To design a home page and another internal skeleton page for a website following our requirements specification and wireframe layout/structure

Task description
We are looking for a modern, attractive, clean design for our new website to reflect our businesses professionalism and high quality services that we offer.
• www.brelvox.com
• www.quintaro.com
We would like a design for a home page and one other skeleton subpage for our website. We have provided a wireframe image to assist, showing how we would like the layout/structure of our website to follow which also highlights where we would like specific content/features to go.
We have listed what features the site must have in the requirements section.
The final design should communicate to our users that we are a professional business that offer high quality services and that we are a company they can trust and rely on.

Look and feel
The wireframe we have attached is a representation of how we would like the layout and structure of the website to be designed. We would like to have a corporate theme to our website.

Colours
Open to interpretation by the designer, as long as the colours suit a corporate theme and give off a professional look and feel.

Requirements
The design must have the following:

General
• Home page design (Based on attached wireframe).
• Internal Page design (This needs to be a skeleton page which can be used for implemented the content for all over pages).

• Contact details to be visible on every page, contact number at the header and all other relative details in the footer section.
• Social networking icons within the footer section of the site.
• Avoid the use of unprofessional images for buttons, icons and banners etc.
Features desired
• Drop down navigation bar. Please see the attached image for inspiration for its design/layout.
o We would like a similar drop down menu design to the one on this site: www.tdmq.co.uk.
• Image slider at the header of every page just beneath the navigation bar.
o We would like the Plexa slider to be used for the image slider. Please use this link for an example of it in action: http://www.scriptloomhub.net/demo/plexa-slider/
o The image slider needs to be larger on the home page.
o The image slider can be smaller on the rest of the pages of the site.
• Chirply feed present on every page.
• News/Blog feed present on every page.
• Call back form present on every page.
• Wayfindr Map implementation above footer on every page.

A user friendly, accessible design that is easy to use and easy for the user to understand. Must have a corporate theme to reflect the professionalism of our business. Content flows logically and keep content spaced out so that it does not make the site look cluttered.

Target Market(s)

Small to Mid sized Business, Large Banks and Legal, corporate, business - non-technical users

Industry/Entity Type

Business

Font styles to use
Sans Serif

```html
<!DOCTYPE html>
<html lang="en">
<head>
<meta charset="utf-8">
<title>Tidewell Systems – IT Support &amp; Cloud Services</title>
<link href="https://fonts.googleapis.com/css2?family=Open+Sans:wght@400;600;700&family=Oswald:wght@400;500&display=swap" rel="stylesheet">
<style>
:root{
  --blue:#1b8fd6;
  --blue-dark:#0f6fae;
  --navy:#183a5a;
  --nav:#1d2e3f;
  --ink:#333;
  --muted:#777;
  --line:#dcdcdc;
  --panel:#f3f3f3;
  --footer:#2b2f33;
  --footer-bottom:#1f2326;
}
*{box-sizing:border-box;margin:0;padding:0}
html,body{width:1200px;height:2868px;overflow:hidden}
body{font-family:"Open Sans",Arial,sans-serif;color:var(--ink);background:#fff;font-size:14px;line-height:1.55;position:relative}
.wrap{width:1100px;margin:0 auto;position:relative}
h2,h3,h4{font-family:"Oswald","Open Sans",sans-serif;font-weight:400;letter-spacing:.5px}

/* header */
.site-header{height:120px}
.site-header .wrap{height:120px;display:flex;align-items:center;justify-content:space-between}
.brand{display:flex;align-items:center;gap:12px;font-size:30px;font-weight:600;color:var(--blue)}
.brand-mark{width:26px;height:26px;border-radius:50%;background:var(--blue)}
.contact-top{text-align:right}
.contact-top .label{font-family:"Oswald",sans-serif;color:var(--blue);font-size:22px;letter-spacing:1px}
.contact-top .phone{font-size:26px;font-weight:700;color:var(--navy);display:flex;gap:8px;align-items:center;justify-content:flex-end}
.contact-top .mail{font-size:14px;color:var(--muted)}

/* nav */
.main-nav{background:var(--nav);height:40px;position:relative;z-index:5}
.main-nav ul{list-style:none;display:flex;height:40px}
.main-nav li{color:#fff;font-size:13px;font-weight:600;padding:0 22px;line-height:40px;text-transform:uppercase}
.main-nav li.active{background:var(--blue)}
.dropdown{position:absolute;top:40px;left:50px;width:520px;height:200px;background:var(--nav);display:flex;padding:14px;gap:16px}
.dropdown ul{display:block;height:auto;width:130px}
.dropdown li{line-height:26px;font-size:11px;font-weight:400;text-transform:none;padding:0 6px;border-bottom:1px solid rgba(255,255,255,.12)}
.dropdown .case{flex:1;color:#fff}
.dropdown .case h4{font-size:15px;margin-bottom:6px}
.case-img{height:140px;background:linear-gradient(135deg,#3a7fc4,#9ccaf0)}

/* hero */
.hero{height:280px;display:flex}
.hero-img{width:600px;background:linear-gradient(120deg,#2c4a63,#6f8ea8 55%,#c9d7e3)}
.hero-copy{flex:1;background:var(--blue);color:#fff;padding:50px 60px 0 40px}
.hero-copy h1{font-family:"Oswald",sans-serif;font-weight:500;font-size:32px;line-height:1.15;margin-bottom:14px}
.ticks{list-style:none;font-size:14px}
.ticks li{display:flex;gap:8px;align-items:center;margin-bottom:4px}
.btn{display:inline-block;background:#fff;color:var(--blue);font-weight:700;font-size:13px;padding:9px 22px;margin-top:16px;margin-left:120px;border-radius:2px}

/* services */
.services{background:var(--blue-dark);height:200px;color:#fff}
.services .wrap{display:flex;height:200px;align-items:center}
.service{flex:1;text-align:center;padding:0 18px}
.service svg{display:block;margin:0 auto 10px}
.service h3{font-size:22px;text-transform:uppercase;line-height:1.1;margin-bottom:6px}
.service p{font-size:12px;opacity:.9}

/* main */
.content{display:flex;gap:40px;padding-top:30px;height:1180px}
.primary{width:770px}
.sidebar{flex:1}
.sec-title{font-size:26px;color:var(--navy);border-bottom:1px solid var(--line);padding-bottom:6px;margin-bottom:14px;text-transform:uppercase}
.welcome p{font-size:13px;margin-bottom:14px;color:#555}
.welcome-top{display:flex;gap:24px}
.welcome-top .txt{flex:1}
.welcome-img{width:300px;height:200px;background:linear-gradient(135deg,#cfd8e2,#8aa3bc)}
.welcome .ticks li{color:#444;font-size:13px}

.feedback{background:var(--panel);padding:20px 24px;margin-top:30px;height:230px;position:relative}
.quotes{display:flex;gap:40px}
.quote{flex:1;font-style:italic;font-size:13px;color:#555}
.who{display:flex;gap:10px;align-items:center;margin-top:10px;font-style:normal}
.avatar{width:40px;height:40px;background:#b8c3cd}
.who b{color:var(--blue);display:block;font-size:13px}
.who span{font-size:12px;color:var(--muted)}
.quote-mark{position:absolute;right:40px;bottom:30px}

.form-box input,.form-box textarea{display:block;width:100%;border:1px solid var(--line);margin-bottom:8px;padding:7px;font:12px "Open Sans",sans-serif;color:#999;background:#fff}
.form-box textarea{height:90px}
.form-box p{font-size:12px;color:#555;margin-bottom:10px}
.submit{background:var(--blue);color:#fff;font-weight:700;font-size:12px;padding:8px 24px;float:right}
.feed{border:1px solid var(--line);margin-top:40px;clear:both;height:320px;padding:10px}
.feed h4{font-size:15px;border-bottom:1px solid var(--line);padding-bottom:4px}
.tweet{display:flex;gap:10px;padding:10px 0;border-bottom:1px solid #eee;font-size:11px;color:#555}
.tweet .pic{width:36px;height:36px;flex:none;background:var(--blue)}
.news{margin-top:24px}
.news-item{display:flex;gap:12px;margin-bottom:14px}
.news-item .pic{width:80px;height:60px;flex:none;background:linear-gradient(135deg,#7aa6cf,#2f5f8f)}
.news-item h5{font-size:13px;color:var(--blue)}
.news-item p{font-size:11px;color:#666}
.see-all{background:var(--blue);color:#fff;font-size:11px;font-weight:700;padding:6px 14px;float:right}

/* partners */
.partners{height:200px;text-align:center;padding-top:20px}
.partners h2{font-size:26px;color:var(--navy);margin-bottom:26px}
.badges{display:flex;justify-content:center;gap:24px}
.badge{width:160px;height:80px;background:#e6e6e6;border:1px solid #d2d2d2}

.map{height:520px;background:linear-gradient(160deg,#e4e4e4,#cfcfcf)}

/* footer */
.site-footer{background:var(--footer);color:#bbb;height:270px}
.site-footer .wrap{display:flex;gap:50px;padding-top:30px}
.site-footer h4{color:#fff;font-size:15px;text-transform:uppercase;border-bottom:1px solid #444;padding-bottom:6px;margin-bottom:12px}
.f-links{width:230px;list-style:none;font-size:12px}
.f-links li{line-height:26px}
.f-about{flex:1;font-size:12px}
.f-contact{width:300px;font-size:12px}
.f-contact div{display:flex;gap:10px;align-items:center;margin-bottom:10px}
.social{display:flex;gap:8px;float:right;margin-top:-4px}
.social i{width:18px;height:18px;border-radius:50%;background:#666;display:block}
.bottom-bar{background:var(--footer-bottom);height:58px;color:#888;font-size:11px;text-align:center;line-height:58px}
</style>
</head>
<body>
<header class="site-header">
  <div class="wrap">
    <div class="brand"><span class="brand-mark"></span>Tidewell Systems</div>
    <div class="contact-top">
      <div class="label">CONTACT US NOW</div>
      <div class="phone"><svg width="22" height="22" viewBox="0 0 24 24"><path fill="#1b8fd6" d="M6.6 10.8a15.1 15.1 0 0 0 6.6 6.6l2.2-2.2c.3-.3.7-.4 1-.2 1.1.4 2.3.6 3.6.6.6 0 1 .4 1 1V20c0 .6-.4 1-1 1A17 17 0 0 1 3 4c0-.6.4-1 1-1h3.5c.6 0 1 .4 1 1 0 1.3.2 2.5.6 3.6.1.3 0 .7-.2 1z"/></svg>+44 141 555 0192</div>
      <div class="mail">info@tidewell-systems.com</div>
    </div>
  </div>
</header>

<nav class="main-nav">
  <div class="wrap">
    <ul>
      <li>Home</li><li class="active">Products ▾</li><li>Company</li><li>Blog</li><li>Contact Us</li>
    </ul>
    <div class="dropdown">
      <ul><li>Lorem ipsum dolor</li><li>Consectetur adipisc</li><li>Sed diam nonummy</li><li>Pharetra venenatis</li><li>Ut enim ad minim</li><li>Ex lorem convallis</li></ul>
      <ul><li>Lorem ipsum dolor</li><li>Consectetur adip</li><li>Vitae nibh ante</li><li>Pharetra nisi</li></ul>
      <div class="case"><h4>See Our Case Studies</h4><div class="case-img" role="img" aria-label="Cloud computing case study banner"></div></div>
    </div>
  </div>
</nav>

<section class="hero">
  <div class="hero-img" role="img" aria-label="Business professional working in an office"></div>
  <div class="hero-copy">
    <h1>LOREM IPSUM DOLOR SIT AMET<br>CONDIME NTUM PLACERAT</h1>
    <ul class="ticks">
      <li><svg width="14" height="14" viewBox="0 0 14 14"><circle cx="7" cy="7" r="7" fill="#fff"/><path d="M3.5 7l2.5 2.5 4.5-5" stroke="#1b8fd6" stroke-width="2" fill="none"/></svg>Lorem ipsum dolor sit amet consectetur</li>
      <li><svg width="14" height="14" viewBox="0 0 14 14"><circle cx="7" cy="7" r="7" fill="#fff"/><path d="M3.5 7l2.5 2.5 4.5-5" stroke="#1b8fd6" stroke-width="2" fill="none"/></svg>Pellentesque rhoncus magna in tellus</li>
      <li><svg width="14" height="14" viewBox="0 0 14 14"><circle cx="7" cy="7" r="7" fill="#fff"/><path d="M3.5 7l2.5 2.5 4.5-5" stroke="#1b8fd6" stroke-width="2" fill="none"/></svg>Aliquip cing elit sit amet metus at lorem</li>
    </ul>
    <span class="btn">LEARN MORE</span>
  </div>
</section>

<section class="services">
  <div class="wrap">
    <div class="service">
      <svg width="70" height="70" viewBox="0 0 70 70"><circle cx="35" cy="35" r="33" fill="none" stroke="#fff" stroke-width="2"/><rect x="20" y="22" width="30" height="20" fill="none" stroke="#fff" stroke-width="2"/><path d="M28 48h14M35 42v6" stroke="#fff" stroke-width="2"/></svg>
      <h3>IT Support</h3><p>Lorem ipsum dolor sit amet, consectetur adipiscing elit. Ut sit amet metus ut nam mattis.</p>
    </div>
    <div class="service">
      <svg width="70" height="70" viewBox="0 0 70 70"><circle cx="35" cy="35" r="33" fill="none" stroke="#fff" stroke-width="2"/><circle cx="35" cy="24" r="5" fill="#fff"/><circle cx="22" cy="46" r="5" fill="#fff"/><circle cx="48" cy="46" r="5" fill="#fff"/><path d="M35 29v8M35 37L22 46M35 37l13 9" stroke="#fff" stroke-width="2"/></svg>
      <h3>Free Network Audit</h3><p>Lorem ipsum dolor sit amet, consectetur adipiscing elit. Ut sit amet metus ut nam mattis.</p>
    </div>
    <div class="service">
      <svg width="70" height="70" viewBox="0 0 70 70"><circle cx="35" cy="35" r="33" fill="none" stroke="#fff" stroke-width="2"/><path d="M22 44h26a8 8 0 0 0 0-16 11 11 0 0 0-21-2 9 9 0 0 0-5 18z" fill="none" stroke="#fff" stroke-width="2"/></svg>
      <h3>Backup &amp; Cloud<br>Solutions</h3><p>Lorem ipsum dolor sit amet, consectetur adipiscing elit. Ut sit amet metus.</p>
    </div>
    <div class="service">
      <svg width="70" height="70" viewBox="0 0 70 70"><circle cx="35" cy="35" r="33" fill="none" stroke="#fff" stroke-width="2"/><rect x="19" y="24" width="32" height="22" fill="none" stroke="#fff" stroke-width="2"/><path d="M19 24l16 12 16-12" fill="none" stroke="#fff" stroke-width="2"/></svg>
      <h3>Hosted Mailvane</h3><p>Lorem ipsum dolor sit amet, consectetur adipiscing elit. Ut sit amet metus ut nam mattis.</p>
    </div>
  </div>
</section>

<main class="wrap content">
  <div class="primary">
    <section class="welcome">
      <h2 class="sec-title">Welcome</h2>
      <div class="welcome-top">
        <div class="txt">
          <p>For many companies today, IT support is a large part of doing business. It is not always possible for a company or business to have a dedicated IT support team. For companies and businesses in Kelmont, Tidewell Systems is the answer to IT needs.</p>
          <p>Lorem ipsum dolor sit amet, consectetur adipiscing elit. Vivamus tincidunt, lorem eu tristique consectetur, magna nibh convallis urna.</p>
          <ul class="ticks">
            <li><svg width="14" height="14" viewBox="0 0 14 14"><circle cx="7" cy="7" r="7" fill="#1b8fd6"/><path d="M3.5 7l2.5 2.5 4.5-5" stroke="#fff" stroke-width="2" fill="none"/></svg>Lorem ipsum dolor sit amet consectetur adipiscing elit</li>
            <li><svg width="14" height="14" viewBox="0 0 14 14"><circle cx="7" cy="7" r="7" fill="#1b8fd6"/><path d="M3.5 7l2.5 2.5 4.5-5" stroke="#fff" stroke-width="2" fill="none"/></svg>Pellentesque rhoncus magna in tellus luctus</li>
            <li><svg width="14" height="14" viewBox="0 0 14 14"><circle cx="7" cy="7" r="7" fill="#1b8fd6"/><path d="M3.5 7l2.5 2.5 4.5-5" stroke="#fff" stroke-width="2" fill="none"/></svg>Pellentesque congue purus vitae ante</li>
          </ul>
        </div>
        <div class="welcome-img" role="img" aria-label="Laptop and office desk illustration"></div>
      </div>
      <p>Etiam tempus orci quis massa sagittis sit amet lobortis quam malesuada. In interdum blandit viverra. Vivamus malesuada arcu in tellus consectetur rhoncus. Lorem ipsum dolor sit amet, consectetur adipiscing elit. Pellentesque rhoncus.</p>
      <p>Mauris in tellus luctus gravida. Donec nisi diam, imperdiet eu pulvinar eget, faucibus eu mi. Integer velit erat, blandit a ullamcorper id, volutpat et quam.</p>
      <p>Maecenas ultrices arcu eget porta ultricies in mollis lacus congue. Nullam sem tortor, volutpat non eleifend ut, pellentesque in augue. Aliquam dictum magna. Etiam tempus orci quis massa sagittis sit amet lobortis quam malesuada. In interdum blandit viverra. Vivamus malesuada arcu in tellus consectetur rhoncus. Lorem ipsum dolor sit amet, consectetur adipiscing elit. Pellentesque rhoncus magna in tellus luctus gravida. Donec nisi diam, imperdiet eu pulvinar eget, faucibus eu mi. Integer velit erat, blandit a ullamcorper id, volutpat et quam. Cras volutpat odio sit amet malesuada. Proin et ipsum quis lacus ornare sit mollis. Etiam tempus orci quis massa sagittis sit amet lobortis quam.</p>
      <p>Nullam iaculis lacinia tortor mollis vitae, vitae consectetur ut condimentum pulvinar scelerisque. Sed tellus erat, pellentesque id amet eleifend quis, ultricies ut sapien. Donec vehicula egestas sollicitudin. Mauris suscipit rutrum dignissim. Sed vitae libero eget erat tincidunt condimentum eget quis mauris. Aliquam gravida blandit velit, vitae posuere lacus imperdiet nec. Pellentesque in orci id est venenatis tristique. Ut at eros nec nisl sollicitudin adipiscing sit amet ante. Maecenas pharetra auctor magna, vitae consectetur tortor iaculis et.</p>
      <p>Cum sociis natoque penatibus et magnis dis parturient montes, nascetur ridiculus mus. Proin suscipit nisi non eros malesuada dapibus non vel tellus. Donec quam massa, aliquam id rhoncus laoreet.</p>
    </section>

    <section class="feedback">
      <h2 class="sec-title">Clients Feedback</h2>
      <div class="quotes">
        <div class="quote">"We have used Tidewell Systems Ltd for many IT services across a number of companies that I have been involved with. They are dedicated professionals who always deliver results in a timely manner."
          <div class="who"><div class="avatar" role="img" aria-label="Client photo"></div><div><b>Alan Rennick</b><span>Harlow Joinery</span></div></div>
        </div>
        <div class="quote">"Tidewell Systems are smart, intuitive, structured and analytical thinkers who provides great advice and valuable support – always in a cheerful and positive manner."
          <div class="who"><div class="avatar" role="img" aria-label="Client photo"></div><div><b>Moira T</b><span>Clyde Fieldworks</span></div></div>
        </div>
      </div>
      <svg class="quote-mark" width="50" height="40" viewBox="0 0 50 40"><path d="M0 0h20v20l-8 20H4l6-20H0zM28 0h20v20l-8 20h-8l6-20h-10z" fill="#1b8fd6"/></svg>
    </section>
  </div>

  <aside class="sidebar">
    <section class="form-box">
      <h2 class="sec-title">Contact Us</h2>
      <p>Be guaranteed to respond within one hour. Alternatively call us on +44 141 555 0192.</p>
      <input value="Insert Your Name"><input value="Insert Your Email"><input value="Insert Your Phone"><textarea>Insert Your Message</textarea>
      <span class="submit">SUBMIT</span>
    </section>
    <section class="feed">
      <h4>Chirply <span style="font-size:11px;color:#999">@TidewellSys</span></h4>
      <div class="tweet"><div class="pic"></div><div><b>Tidewell Systems</b><br>Lightning-fast office cloud backup now live for all of our clients.</div></div>
      <div class="tweet"><div class="pic"></div><div><b>Tidewell Systems</b><br>Five quick checks to keep your network secure this winter.</div></div>
      <div class="tweet"><div class="pic"></div><div><b>Tidewell Systems</b><br>Hosted email migration complete for another happy client.</div></div>
      <div class="tweet"><div class="pic"></div><div><b>Tidewell Systems</b><br>Free network audit places still open this month. Book now.</div></div>
    </section>
    <section class="news">
      <h2 class="sec-title">Latest News</h2>
      <div class="news-item"><div class="pic" role="img" aria-label="News thumbnail"></div><div><h5>Why Our Competitors Hate Us...</h5><p>You are now in the correct place to be [...]</p></div></div>
      <div class="news-item"><div class="pic" role="img" aria-label="News thumbnail"></div><div><h5>Kelmont Small Business Switch to Cloud Based Software</h5><p>Cloud based systems rising fast [...]</p></div></div>
      <div class="news-item"><div class="pic" role="img" aria-label="News thumbnail"></div><div><h5>Four Things To Check</h5><p>When you hire IT consultants, you [...]</p></div></div>
      <span class="see-all">SEE ALL NEWS</span>
    </section>
  </aside>
</main>

<section class="partners">
  <h2>OUR PARTNERS</h2>
  <div class="badges"><div class="badge"></div><div class="badge"></div><div class="badge"></div><div class="badge"></div><div class="badge"></div><div class="badge"></div></div>
</section>

<section class="map" role="img" aria-label="Wayfindr Map showing office location"></section>

<footer class="site-footer">
  <div class="wrap">
    <div><h4>Quick Links</h4>
      <ul class="f-links"><li>› Home</li><li>› Products</li><li>› Company</li><li>› Blog</li><li>› Contact Us</li></ul>
    </div>
    <div class="f-about"><h4>About Us</h4>
      <p>Tidewell Systems Limited provide Business IT Support to companies in Kelmont and Bayside. Some of our services include Managed IT Support, Hosted Mailvane, Online backup and Cloud Solutions. Read More</p>
    </div>
    <div class="f-contact"><h4>Contact Us <span class="social"><i></i><i></i><i></i><i></i></span></h4>
      <div><svg width="14" height="14" viewBox="0 0 24 24"><path fill="#1b8fd6" d="M12 2a7 7 0 0 0-7 7c0 5 7 13 7 13s7-8 7-13a7 7 0 0 0-7-7zm0 9.5A2.5 2.5 0 1 1 12 6.5a2.5 2.5 0 0 1 0 5z"/></svg>Tidewell Systems Limited, 20 Marsh Street, Kelmont, G2 4AA</div>
      <div><svg width="14" height="14" viewBox="0 0 24 24"><path fill="#1b8fd6" d="M6.6 10.8a15.1 15.1 0 0 0 6.6 6.6l2.2-2.2c.3-.3.7-.4 1-.2 1.1.4 2.3.6 3.6.6.6 0 1 .4 1 1V20c0 .6-.4 1-1 1A17 17 0 0 1 3 4c0-.6.4-1 1-1h3.5c.6 0 1 .4 1 1 0 1.3.2 2.5.6 3.6.1.3 0 .7-.2 1z"/></svg>+44 141 555 0192</div>
      <div><svg width="14" height="14" viewBox="0 0 24 24"><rect x="2" y="5" width="20" height="14" fill="none" stroke="#1b8fd6" stroke-width="2"/><path d="M2 5l10 8 10-8" fill="none" stroke="#1b8fd6" stroke-width="2"/></svg>info@tidewell-systems.com</div>
    </div>
  </div>
</footer>
<div class="bottom-bar">Copyright © 2016 Tidewell Systems Limited. All Rights Reserved. | Privacy Policy | Site Map</div>
</body>
</html>
```